Book cover needed for a major new book on emotional resilience

The book will be titled: 'Stone to Stream: from habit bound to builders of renewal - The guide for growing steady teams and institutions'
My websites are http://www.pathmorrow.com and http://www.lumbrava.org and I am http://en.wikiverse-sample.org/wiki/Martin_Okonedo_(uncertainty_scholar) ad expert in developing emotional resilience. My previous book was The Murky Dividend.
The premise of the book is to introduce brand new material which is the first ever methodology and strategy on how to develop emotional resilience across entire populations like organisations and companies or moving people from fear about change to finding flow through resilience.
The final design should communicate the fact that this is a strategy and methodology. That it is about developing people and entire organisations to be more resilient and who are able to deal with change better.
Target Market(s)
Consultants, Organisational development consultants, Human Resource professionals.

```html
<!DOCTYPE html>
<html lang="en">
<head>
<meta charset="utf-8">
<title>Stone to Stream — Book Cover</title>
<link rel="stylesheet" href="https://fonts.googleapis.com/css2?family=Fira+Sans:wght@400;500;600&display=swap">
<style>
  :root {
    --backdrop: #6b7075;
    --paper: #ffffff;
    --ink: #111111;
    --accent-blue: #1ba1e2;
    --author-grey: #8a8a8a;
    --art-dark: #141414;
    --art-light: #f2f2f2;
  }
  * { margin: 0; padding: 0; box-sizing: border-box; }
  html, body {
    width: 1200px;
    height: 900px;
    overflow: hidden;
    background: var(--backdrop);
  }
  .canvas {
    position: relative;
    width: 1200px;
    height: 900px;
  }
  .book-cover {
    position: absolute;
    left: 316px;
    top: 20px;
    width: 568px;
    height: 852px;
    background: var(--paper);
    font-family: "Fira Sans", sans-serif;
  }
  .cover-title {
    position: absolute;
    left: 30px;
    top: 22px;
    font-size: 62px;
    font-weight: 600;
    line-height: 1;
    letter-spacing: -0.5px;
    color: var(--ink);
  }
  .cover-subtitle {
    position: absolute;
    left: 36px;
    top: 92px;
    font-size: 29px;
    font-weight: 500;
    line-height: 1.17;
    color: var(--accent-blue);
  }
  .cover-tagline {
    position: absolute;
    left: 36px;
    top: 170px;
    font-size: 14.5px;
    font-weight: 500;
    letter-spacing: 0.2px;
    text-transform: uppercase;
    color: var(--ink);
  }
  .cover-art {
    position: absolute;
    left: 0;
    top: 198px;
    width: 568px;
    height: 558px;
    background:
      radial-gradient(ellipse at 52% 50%, var(--art-light) 0%, #8a8a8a 35%, var(--art-dark) 70%, #6a6a6a 100%);
  }
  .cover-author {
    position: absolute;
    left: 30px;
    top: 778px;
    font-size: 31px;
    font-weight: 500;
    color: var(--author-grey);
  }
</style>
</head>
<body>
  <div class="canvas">
    <article class="book-cover">
      <h1 class="cover-title">Stone to Stream:</h1>
      <p class="cover-subtitle">from Habit Bound<br>to Builders of Renewal</p>
      <p class="cover-tagline">The guide for growing steady teams and institutions</p>
      <div class="cover-art" role="img" aria-label="Black and white op-art striped vortex twisting into the centre"></div>
      <p class="cover-author">Martin J. Okonedo</p>
    </article>
  </div>
</body>
</html>
```